Webdesign für vielseitiges Unternehmen
Zielgruppe
Die Seite wird HOCHMOOR-ART oder DESIGN heißen.
Das Unternehmen bietet folgende Segmente an:
1. Möbelstücke (meist Unikate, da restauriert mit eigener Kreation)
2. Fotografien
3. Malerei
4. Interieurdesign (Gestalten, Einrichten von Apartments, Häusern, Shops etc.) (hier muss natürlich mehr Platz für Informationstext sein.
5. Gallery. - Infos zu Öffnungszeiten und Bilder ebenfalls.
6. Die Location ist für Events buchbar
(7.) Blogg wenns nicht zu aufwändig ist. (hier möchte ich gern Bilder posten die ich irgendwo finde und als gut erachte. Oder Produkte. Wichtig ist, dass bei Verbreitung von Fremdpostings, immer die Quelle eingefügt werden muss. Am besten automatisch. Ich muss zu dem Post noch eigenes Kommentar abgeben können.
Für jedes Segment soll eine Unterseite geschaffen werden.
Die Produktfotos sollen clean aufgebaut sein. Am besten je Produkt 1 Bild pro Seite. Vielleicht erst nachdem man auf ein Bild in der Auswahl geklickt hat?? 3 nebeneinander und dann neue Zeile.
Unter den Bildern (hauptsächlich Querformat aber Hochformat muss auch gehen) müssen Angaben stehen:
-Art
-Size
-Auflage
-Preis
-liken für Social Media oder weiterleiten (wenn möglich)
-Fragen zu diesem Produkt ( wenn hier jemand klickt und etwas schreibt, muss ich eine mail erhalten, wo ich direkt ersehen kann, zu welchem Produkt die Frage zugeordnet ist.
Pro Artikel müssen mehrere Bilder eingestellt werden können, die der Client durch einfaches klicken durchklicken kann.
Die Seite soll clean, chic und Edel wirken. Hauptsächlich über Bilder. Shopsystem ist wegen Aufwandskosten erstmal nicht geplant)
Ich muss die Seite selber pflegen können, auch SEO Optimieren (ohne Programierkenntnisse)
Die Seite soll eine Seite für verschiedene Aspekte sein wie:
- Gallerie
hier wird die Gallerie vorgestellt und Bilder gezeigt von Ausstellungen und Künstlervorstellung..
Aufgabenstellung
Schwarz- Weiß
Akzente eventuell in Patinagrün oder Grünspan oder Malachitgrün oder Gold
Mobilgeräte responsiv

```html
<!DOCTYPE html>
<html lang="de">
<head>
<meta charset="utf-8">
<title>HOCHMOOR – Interieur · Design · Galerie</title>
<link rel="stylesheet" href="https://fonts.googleapis.com/css2?family=Source+Sans+3:wght@300;400;600;700&display=swap">
<style>
  :root {
    --green: #2f5f35;
    --green-soft: #5d8a68;
    --nav-grey: #a9a9a9;
    --ink: #1c1c1c;
    --line: #2f5f35;
    --footer-bg: #f5f5f5;
    --white: #ffffff;
    --placeholder: #8a8f93;
  }
  * { box-sizing: border-box; margin: 0; padding: 0; }
  html, body { width: 992px; height: 1200px; overflow: hidden; background: var(--white); }
  body { position: relative; font-family: "Source Sans 3", "Myriad Pro", sans-serif; color: var(--ink); }

  .brand { position: absolute; top: 24px; left: 0; width: 992px; text-align: center; }
  .brand-name { font-size: 24px; font-weight: 400; letter-spacing: 2px; color: var(--ink); line-height: 1; }
  .brand-tagline { font-size: 6px; letter-spacing: 2.5px; margin-top: 5px; color: var(--ink); }

  .main-nav a { position: absolute; top: 80px; font-size: 13px; font-weight: 300; color: var(--nav-grey); text-decoration: none; text-transform: uppercase; white-space: nowrap; }
  .main-nav a.is-active { color: var(--green-soft); }
  .main-nav a.is-active::after { content: ""; position: absolute; left: -9px; right: -9px; bottom: -3px; border-bottom: 1px solid var(--green-soft); }
  .main-nav a.nav-cta { top: 74px; left: 769px; width: 70px; height: 29px; line-height: 27px; text-align: center; border: 1px solid var(--green-soft); border-radius: 4px; color: var(--green-soft); }

  .hero { position: absolute; left: 0; top: 128px; width: 992px; height: 525px; overflow: hidden; }
  .hero-media { position: absolute; inset: 0; background:
      radial-gradient(ellipse at 55% 60%, #b7a796 0%, transparent 45%),
      linear-gradient(100deg, #c8ccd0 0%, #e3e1dc 35%, #d9d3cb 55%, #9b8977 80%, #6e5e50 100%); }
  .hero-shade { position: absolute; inset: 0; background: linear-gradient(180deg, transparent 55%, rgba(0,0,0,.28) 100%); }
  .hero-arrow { position: absolute; top: 243px; width: 44px; height: 44px; }
  .hero-arrow.prev { left: 21px; }
  .hero-arrow.next { left: 926px; }
  .hero-title { position: absolute; left: 47px; top: 417px; font-size: 33px; font-weight: 600; color: var(--white); }
  .hero-text { position: absolute; left: 47px; top: 467px; font-size: 13px; font-weight: 600; color: var(--white); }
  .hero-button { position: absolute; left: 828px; top: 464px; width: 126px; height: 37px; line-height: 35px; text-align: center; border: 2px solid var(--white); border-radius: 4px; color: var(--white); font-size: 13px; font-weight: 600; }
  .hero-dots { position: absolute; left: 466px; top: 499px; width: 70px; height: 14px; }

  .contact-title { position: absolute; top: 694px; left: 0; width: 992px; text-align: center; font-size: 34px; font-weight: 400; color: var(--green); }
  .field { position: absolute; border: 1px solid var(--line); border-radius: 3px; font-size: 13px; color: var(--placeholder); padding-left: 13px; background: var(--white); }
  .field-input { left: 246px; width: 237px; height: 39px; line-height: 37px; }
  .field-message { left: 508px; top: 754px; width: 237px; height: 163px; padding-top: 12px; padding-left: 16px; }
  .submit { position: absolute; left: 443px; top: 937px; width: 106px; height: 33px; line-height: 31px; text-align: center; border: 1px solid var(--line); border-radius: 3px; color: var(--green); font-size: 13px; }

  .site-footer { position: absolute; left: 0; top: 1025px; width: 992px; height: 175px; background: var(--footer-bg); }
  .footer-col { position: absolute; top: 36px; list-style: none; font-size: 12px; color: var(--ink); }
  .footer-col li { height: 25.5px; }
  .footer-col.social li { position: relative; padding-left: 22px; }
  .footer-col.social li::before { content: ""; position: absolute; left: 0; top: 2px; width: 9px; height: 9px; border: 1px solid var(--ink); border-radius: 50%; }
</style>
</head>
<body>
  <header>
    <div class="brand">
      <div class="brand-name">HOCHMOOR</div>
      <div class="brand-tagline">INTERIEUR · DESIGN · GALERIE</div>
    </div>
    <nav class="main-nav">
      <a class="is-active" style="left:162px">Home</a>
      <a style="left:227px">Über Uns</a>
      <a style="left:324px">Gallerie</a>
      <a style="left:415px">Fotografie</a>
      <a style="left:524px">Malerei</a>
      <a style="left:611px">Interieur</a>
      <a style="left:710px">Blog</a>
      <a class="nav-cta">Kontakt</a>
    </nav>
  </header>

  <section class="hero">
    <div class="hero-media" role="img" aria-label="Foto: Team im Gespräch in einem hellen Büro"></div>
    <div class="hero-shade"></div>
    <svg class="hero-arrow prev" viewBox="0 0 44 44"><circle cx="22" cy="22" r="22" fill="rgba(0,0,0,.12)"/><path d="M25 14 L17 22 L25 30" fill="none" stroke="#fff" stroke-width="3.5" stroke-linecap="round" stroke-linejoin="round"/></svg>
    <svg class="hero-arrow next" viewBox="0 0 44 44"><path d="M19 14 L27 22 L19 30" fill="none" stroke="#fff" stroke-width="3.5" stroke-linecap="round" stroke-linejoin="round"/></svg>
    <h2 class="hero-title">Über Uns</h2>
    <p class="hero-text">Hier ein kurzer text über das team oder das Unternehmen.</p>
    <div class="hero-button">MEHR SEHEN</div>
    <svg class="hero-dots" viewBox="0 0 70 14">
      <circle cx="7" cy="7" r="5" fill="none" stroke="#fff" stroke-width="1"/>
      <circle cx="7" cy="7" r="2.6" fill="#fff"/>
      <circle cx="26" cy="7" r="2.4" fill="rgba(255,255,255,.8)"/>
      <circle cx="40" cy="7" r="2.4" fill="rgba(255,255,255,.6)"/>
      <circle cx="55" cy="7" r="2.4" fill="rgba(255,255,255,.4)"/>
    </svg>
  </section>

  <section class="contact">
    <h2 class="contact-title">Kontakt</h2>
    <div class="field field-input" style="top:754px">Name</div>
    <div class="field field-input" style="top:815px">Email</div>
    <div class="field field-input" style="top:876px">Anliegen</div>
    <div class="field field-message">Nachricht</div>
    <div class="submit">ABSCHICKEN</div>
  </section>

  <footer class="site-footer">
    <ul class="footer-col" style="left:47px"><li>Über Uns</li><li>Blog</li><li>Datenschutz</li><li>Impressum</li></ul>
    <ul class="footer-col" style="left:283px"><li>Gallerie</li><li>Fotografie</li><li>Malerei</li><li>Intereur</li></ul>
    <ul class="footer-col" style="left:568px"><li>Hochmoor 12a</li><li>12345 Musterstadt</li><li>T. +49 123 123 1234</li><li>info@hochmoor-art.de</li></ul>
    <ul class="footer-col social" style="left:830px"><li>Freundeskreis</li><li>Kurzpost</li><li>Bildstrom</li></ul>
  </footer>
</body>
</html>
```